Industrial/Commercial Plumbing Capability Statement

Would like a construction capability statement/Brochure amended to be similar to the attached. -
Have included photos and Notes on the attached
would like project photos to be used
This is a previous capability statement that we would like amended and altered to include, safety, QA and Recent Projects
Please use our company logo
Updates

Need extra days to review

Target Market(s)

Construction work - Industrial

Industry/Entity Type

Plumbing

Requirements
Must have
• Include all items in contents page

Eye Catching Photos relevant to construction industry and relevant to topic on page

```html
<!DOCTYPE html>
<html lang="en">
<head>
<meta charset="utf-8">
<title>Ridgeline Plumbers – Capability Statement</title>
<link href="https://fonts.googleapis.com/css2?family=Montserrat:wght@300;400;600;700;800&family=Open+Sans:wght@400;600&display=swap" rel="stylesheet">
<style>
:root{
  --bg:#dcdde2;
  --navy:#1b3766;
  --navy-deep:#0d1c3d;
  --navy-ink:#13284f;
  --mid-blue:#2f5b8c;
  --paper:#f4f5f7;
  --paper-grey:#e6e8ec;
  --rule:#9aa3b3;
  --text:#3d4556;
  --white:#ffffff;
}
*{box-sizing:border-box;margin:0;padding:0}
html,body{width:1200px;height:2387px;overflow:hidden}
body{background:var(--bg);font-family:"Open Sans",Arial,sans-serif;color:var(--text);position:relative}
.spread{position:absolute;left:200px;width:800px;height:566px;display:flex;box-shadow:0 18px 40px rgba(0,0,0,.18)}
.spread--covers{top:115px}
.spread--intro{top:910px}
.spread--about{top:1705px}
.page{position:relative;width:400px;height:566px;overflow:hidden;background:var(--paper)}
.page svg.bg{position:absolute;inset:0}
.brand{font-family:"Montserrat",Arial,sans-serif;font-weight:800;color:var(--navy);letter-spacing:.5px;display:flex;align-items:center;gap:6px;white-space:nowrap}
.brand::before{content:"";width:10px;height:10px;background:var(--navy);display:block}

/* back cover */
.contact{position:absolute;left:22px;bottom:34px;display:flex;align-items:flex-start;gap:12px;font-family:"Montserrat",Arial,sans-serif;color:var(--navy-ink)}
.contact__title{font-weight:800;font-size:12px;line-height:1.05;padding-right:12px;border-right:1.5px solid var(--navy-ink)}
.contact__list{display:grid;grid-template-columns:auto auto;gap:6px 18px;font-size:7.5px;font-weight:600;line-height:1.3}
.contact__item{display:flex;gap:5px;align-items:flex-start}
.contact__item svg{flex:none;margin-top:1px}

/* front cover */
.cover-title{position:absolute;left:40px;top:120px;color:var(--white);font-family:"Montserrat",Arial,sans-serif;line-height:.95}
.cover-title__strong{display:block;font-weight:800;font-size:48px;letter-spacing:-.5px}
.cover-title__light{display:block;font-weight:300;font-size:38px;letter-spacing:3px}
.cover-brand{position:absolute;right:28px;bottom:34px;font-size:17px}

/* contents */
.page--navy{background:linear-gradient(160deg,#1d3a70 0%,#152c59 60%,#0f2248 100%)}
.skyline{position:absolute;left:0;right:0;bottom:0;height:230px;background:linear-gradient(180deg,rgba(15,34,72,0) 0%,rgba(9,22,48,.55) 100%)}
.toc{position:absolute;left:70px;top:80px;width:260px;color:var(--white);font-family:"Montserrat",Arial,sans-serif}
.toc__title{font-weight:700;font-size:14px;line-height:1.1;text-transform:uppercase;margin-bottom:18px;letter-spacing:1px}
.toc__list{list-style:none}
.toc__item{display:flex;gap:14px;font-size:10px;padding:7px 0 6px;border-bottom:1px dashed rgba(255,255,255,.7);text-transform:uppercase;letter-spacing:.6px}
.toc__num{font-weight:600;width:16px}

/* inner pages */
.heading{font-family:"Montserrat",Arial,sans-serif;color:var(--navy);text-transform:uppercase;line-height:1.05}
.heading__light{display:block;font-weight:300;font-size:15px;letter-spacing:1px}
.heading__strong{display:block;font-weight:800;font-size:16px}
.section-tag{display:flex;align-items:center;margin:6px 0 10px}
.section-tag__line{flex:1;height:1px;background:var(--rule)}
.section-tag__dot{width:7px;height:7px;border:1px solid var(--rule);border-radius:50%;margin-right:8px}
.section-tag__label{font-family:"Montserrat",Arial,sans-serif;font-weight:700;font-size:7px;color:var(--navy);letter-spacing:.8px}
.body-copy p{font-size:6.3px;line-height:1.5;margin-bottom:6px}
.subhead{font-family:"Montserrat",Arial,sans-serif;font-weight:800;color:var(--navy);font-size:9px;line-height:1.2;text-transform:uppercase;margin:8px 0 6px}
.inner{position:absolute;left:30px;right:30px;top:36px}
.photo{display:block;border-radius:2px}
.photo--school{height:150px;margin-top:8px;background:linear-gradient(180deg,#6e9fdc 0%,#a9c6ea 45%,#c9c3b1 62%,#a7b59a 80%,#9aa1a6 100%)}
.photo--crane{height:160px;margin-top:8px;background:linear-gradient(200deg,#4f79b0 0%,#c6a57a 45%,#8a5b3a 70%,#3c3f4a 100%)}
.footer{position:absolute;left:0;right:0;bottom:0;height:60px}
.footer .brand{position:absolute;left:28px;top:14px;font-size:10px}
.footer__rule{position:absolute;left:180px;right:24px;top:22px;height:1px;background:var(--rule)}
.footer__url{position:absolute;right:46px;bottom:14px;background:var(--navy);color:var(--white);font-family:"Montserrat",Arial,sans-serif;font-size:7px;padding:4px 14px 4px 12px;border-radius:9px 0 0 9px}
.footer__num{position:absolute;right:22px;bottom:9px;width:24px;height:24px;border-radius:50%;background:var(--navy);color:var(--white);font-family:"Montserrat",Arial,sans-serif;font-size:9px;font-weight:600;display:flex;align-items:center;justify-content:center;border:2px solid var(--white);box-shadow:0 0 0 1px var(--navy)}

/* testimonial page */
.photo--site{position:absolute;inset:0 0 60px 0;background:linear-gradient(180deg,#3f68ad 0%,#7aa0d4 35%,#d8c7a6 65%,#7b6a5b 85%,#4b4a4f 100%)}
.page--testimonial .brand--top{position:absolute;left:0;right:0;top:40px;justify-content:center;font-size:17px}
.quote{position:absolute;left:70px;right:70px;top:120px;background:var(--navy);border-radius:10px;padding:26px 22px 18px;color:var(--white);text-align:center;font-size:6.8px;line-height:1.55}
.quote__mark{position:absolute;left:50%;top:-16px;transform:translateX(-50%);width:32px;height:32px;border-radius:50%;background:var(--navy);border:2px solid var(--white);display:flex;align-items:center;justify-content:center}
.page--testimonial .footer{background:var(--paper)}
</style>
</head>
<body>

<section class="spread spread--covers">
  <div class="page page--back">
    <svg class="bg" width="400" height="566" viewBox="0 0 400 566">
      <rect width="400" height="566" fill="#0d1c3d"/>
      <polygon points="0,440 175,345 400,500 400,566 0,566" fill="#e8eaee"/>
      <polygon points="175,345 400,298 400,500" fill="#2f5b8c"/>
      <line x1="175" y1="345" x2="400" y2="296" stroke="#ffffff" stroke-width="3"/>
    </svg>
    <div class="contact">
      <div class="contact__title">GET IN<br>TOUCH</div>
      <div class="contact__list">
        <div class="contact__item">
          <svg width="8" height="8" viewBox="0 0 24 24"><path fill="#13284f" d="M6.6 10.8a15 15 0 0 0 6.6 6.6l2.2-2.2c.3-.3.7-.4 1-.2 1.1.4 2.3.6 3.6.6.6 0 1 .4 1 1V20c0 .6-.4 1-1 1A17 17 0 0 1 3 4c0-.6.4-1 1-1h3.5c.6 0 1 .4 1 1 0 1.3.2 2.5.6 3.6.1.3 0 .7-.2 1z"/></svg>
          <span>(08) 9000 4821</span>
        </div>
        <div class="contact__item">
          <svg width="8" height="8" viewBox="0 0 24 24"><circle cx="12" cy="12" r="10" fill="#13284f"/><path d="M2 12h20M12 2c3 3 3 17 0 20M12 2c-3 3-3 17 0 20" stroke="#fff" stroke-width="1.5" fill="none"/></svg>
          <span>ridgelineplumbers.com.au</span>
        </div>
        <div class="contact__item">
          <svg width="8" height="8" viewBox="0 0 24 24"><rect x="3" y="6" width="18" height="12" rx="2" fill="#13284f"/><path d="M3 7l9 6 9-6" stroke="#fff" stroke-width="1.5" fill="none"/></svg>
          <span>PO Box 250 Harlow<br>Park DC WA 6000</span>
        </div>
        <div class="contact__item">
          <svg width="8" height="8" viewBox="0 0 24 24"><path fill="#13284f" d="M12 2a7 7 0 0 0-7 7c0 5 7 13 7 13s7-8 7-13a7 7 0 0 0-7-7zm0 9.5A2.5 2.5 0 1 1 12 6.5a2.5 2.5 0 0 1 0 5z"/></svg>
          <span>14 Carden Street Harlow<br>Park WA 6000</span>
        </div>
      </div>
    </div>
  </div>

  <div class="page page--front">
    <svg class="bg" width="400" height="566" viewBox="0 0 400 566" role="img" aria-label="Site photo of a trench with pipework laid on a construction site, under a navy tint">
      <defs>
        <linearGradient id="siteTint" x1="0" y1="0" x2="0.6" y2="1">
          <stop offset="0" stop-color="#2c4a78"/>
          <stop offset="0.55" stop-color="#24406c"/>
          <stop offset="1" stop-color="#1a3158"/>
        </linearGradient>
      </defs>
      <rect width="400" height="566" fill="url(#siteTint)"/>
      <polygon points="400,215 400,566 70,566" fill="#f0f1f4"/>
    </svg>
    <h1 class="cover-title">
      <span class="cover-title__strong">CAPABILITY</span>
      <span class="cover-title__light">STATEMENT</span>
    </h1>
    <div class="brand cover-brand">RIDGELINE PLUMBERS.</div>
  </div>
</section>

<section class="spread spread--intro">
  <div class="page page--navy">
    <div class="skyline" role="img" aria-label="Faint city skyline photo under a navy tint"></div>
    <nav class="toc">
      <h2 class="toc__title">Table<br>of Contents</h2>
      <ol class="toc__list">
        <li class="toc__item"><span class="toc__num">03</span>From the Directors</li>
        <li class="toc__item"><span class="toc__num">04</span>About the Business</li>
        <li class="toc__item"><span class="toc__num">06</span>Our Services</li>
        <li class="toc__item"><span class="toc__num">07</span>Health and Seafty</li>
        <li class="toc__item"><span class="toc__num">08</span>Quality Assurance</li>
        <li class="toc__item"><span class="toc__num">09</span>Recent Project</li>
        <li class="toc__item"><span class="toc__num">10</span>RP Data</li>
        <li class="toc__item"><span class="toc__num">12</span>Meet the Team</li>
      </ol>
    </nav>
  </div>

  <div class="page">
    <div class="inner">
      <h2 class="heading"><span class="heading__light">Message from</span><span class="heading__strong">The Directors</span></h2>
      <div class="section-tag"><span class="section-tag__line"></span><span class="section-tag__dot"></span><span class="section-tag__label">INTRODUCTION</span></div>
      <div class="body-copy">
        <p>Our modern approach to commercial plumbing means every project benefits from current materials, proven techniques and careful planning. As specialists in industrial and commercial work, we stand at the forefront of plumbing in Perth.</p>
        <p>Our dynamic approach keeps us ahead of the field and shows our skill in choosing the right products and installation methods for each project.</p>
        <h3 class="subhead">We work closely with our builders on the scope of works, to guarentee that target are met, and exceeded</h3>
        <p>Ridgeline Plumbers has broad experience across many sectors, from new shopping centres and hospitals to industrial equipment.</p>
        <p>We aim to exceed the expectations of our customers and have a proven record of delivering large projects on time and on budget.</p>
        <p>We pride ourselves on the highest level of on-site management, clear communication and sound problem solving. We stand steadfast on our reputation as flexible, reliable service providers.</p>
        <p>With the right team you avoid costly delays. When you work with us, you deal with trusted specialists in commercial plumbing. We can't wait to start working with you.</p>
      </div>
      <div class="photo photo--school" role="img" aria-label="Photo of a completed school building with a covered basketball court"></div>
    </div>
    <footer class="footer">
      <div class="brand">RIDGELINE PLUMBERS.</div>
      <span class="footer__rule"></span>
      <span class="footer__url">www.ridgelineplumbers.com.au</span>
      <span class="footer__num">01</span>
    </footer>
  </div>
</section>

<section class="spread spread--about">
  <div class="page">
    <div class="inner">
      <h2 class="heading"><span class="heading__light">About the</span><span class="heading__strong">Business</span></h2>
      <div class="section-tag"><span class="section-tag__line"></span><span class="section-tag__dot"></span><span class="section-tag__label">COMPANY</span></div>
      <div class="body-copy">
        <p>Established in 2009 by its directors, Ridgeline Plumbers specialises in commercial and industrial plumbing across Perth, delivering high quality work on projects of every size.</p>
        <p>Our relationships with suppliers and builders are central to our success. We work closely with every client to keep each project safe, compliant and on schedule.</p>
        <p>We strive to lead by example, setting high standards in workmanship, safety and quality assurance, and building teams that take pride in every finished job.</p>
        <p>At Ridgeline Plumbers we believe in training. Our licensed plumbers and apprentices are supported through ongoing development, giving our clients skilled and dependable crews.</p>
        <p>We proudly employ a capable team of full-time staff and apprentices, and we continue to grow a workplace culture that values respect, safety and care.</p>
      </div>
      <div class="photo photo--crane" role="img" aria-label="Photo of workers on a steel-frame construction site with a crane at sunset"></div>
    </div>
    <footer class="footer">
      <div class="brand">RIDGELINE PLUMBERS.</div>
      <span class="footer__rule"></span>
      <span class="footer__url">www.ridgelineplumbers.com.au</span>
      <span class="footer__num">03</span>
    </footer>
  </div>

  <div class="page page--testimonial">
    <div class="photo--site" role="img" aria-label="Photo of two site engineers in hard hats overlooking a building site with cranes"></div>
    <div class="brand brand--top">RIDGELINE PLUMBERS.</div>
    <blockquote class="quote">
      <span class="quote__mark"><svg width="14" height="12" viewBox="0 0 28 24"><path fill="#fff" d="M0 24V13C0 5 4 1 11 0l1 4c-4 1-6 4-6 8h5v12zm16 0V13c0-8 4-12 11-13l1 4c-4 1-6 4-6 8h5v12z"/></svg></span>
      As commercial builders we often have to work on difficult projects that require unique, innovative results. Ridgeline Plumbers are problem solvers and work closely with our team to deliver high quality solution-oriented projects. We started working with them several years ago and continue to be impressed by their professionalism and attention to detail.
    </blockquote>
    <footer class="footer">
      <div class="brand">RIDGELINE PLUMBERS.</div>
      <span class="footer__rule"></span>
      <span class="footer__url">www.ridgelineplumbers.com.au</span>
      <span class="footer__num">02</span>
    </footer>
  </div>
</section>

</body>
</html>
```